Letterhead Design for Tornvale Communications

We are a Telecommunications Company, We wanting to get our Letterhead sorted as the one we have now looks Dull, It be used across our different databases we use but also mainly in Word , I have attached our Logo for you also, our website is tornvale-example.com.au

We would only like to show our postal Address which is PO Box 8164 Korrin Flats NSW 2419

and we need to show our ABN Number Which we would be ABN: 61 482 037 914

Target Market(s)

Looks Stunning for our Proposals and General Usage

Industry/Entity Type

Telecommunications

Requirements
Must have
• Our Postal Address Only and Our ABN Number
Should not have
• Not listing our Actual Address

```html
<!DOCTYPE html>
<html lang="en">
<head>
<meta charset="utf-8">
<title>Tornvale Communications – Letterhead</title>
<link rel="stylesheet" href="https://fonts.googleapis.com/css2?family=Poppins:wght@300;400;500;600&display=swap">
<style>
  :root {
    --backdrop: #66686b;
    --paper: #f1f1f1;
    --ink: #5a5a5a;
    --ink-soft: #6e6e6e;
    --orange: #e0693a;
    --green: #2fa83a;
    --rust: #c8643c;
  }
  * { box-sizing: border-box; margin: 0; padding: 0; }
  html, body {
    width: 1200px; height: 803px; overflow: hidden;
    background: var(--backdrop);
    font-family: "Poppins", sans-serif;
  }
  .letterhead {
    position: absolute; left: 330px; top: 20px;
    width: 540px; height: 763px;
    background: var(--paper);
    color: var(--ink);
  }
  .brand {
    position: absolute; left: 48px; top: 52px;
    display: flex; align-items: center; gap: 8px;
  }
  .brand-dot {
    width: 30px; height: 30px; border-radius: 50%;
    background: var(--orange);
  }
  .brand-name {
    font-size: 15px; font-weight: 500; color: var(--orange);
    letter-spacing: 0.2px;
  }
  .contact {
    position: absolute; right: 36px; top: 44px;
    list-style: none; font-size: 7.5px; font-weight: 300; color: var(--ink);
  }
  .contact li { display: flex; align-items: center; gap: 6px; height: 12.5px; white-space: nowrap; }
  .contact svg { width: 7px; height: 7px; fill: var(--orange); flex: none; }
  .date {
    position: absolute; right: 49px; top: 199px;
    font-size: 10px; font-weight: 300;
  }
  .body {
    position: absolute; left: 48px; top: 226px; width: 443px;
    font-size: 9.6px; font-weight: 300; line-height: 15.3px;
    text-align: justify; color: var(--ink-soft);
  }
  .salutation { font-size: 10px; color: var(--ink); margin-bottom: 12px; }
  .body p + p { margin-top: 21px; }
  .body p.last { margin-top: 25px; }
  .signature {
    position: absolute; left: 46px; top: 594px;
    width: 100px; height: 60px;
    background: linear-gradient(90deg, #e4e4e4, #ececec);
  }
  .footer-address {
    position: absolute; right: 37px; top: 736px;
    font-size: 7.5px; font-weight: 300; color: var(--ink);
    white-space: nowrap;
  }
  .footer-address .sep { margin: 0 5px; color: var(--orange); }
  .footer-bar { position: absolute; left: 0; bottom: 0; width: 540px; height: 9px; }
  .footer-bar span { position: absolute; top: 0; height: 9px; }
  .bar-orange { left: 0; width: 302px; background: var(--orange); }
  .bar-green { left: 304px; width: 206px; background: var(--green); }
  .bar-rust { left: 513px; width: 27px; background: var(--rust); }
</style>
</head>
<body>
<main class="letterhead">
  <header>
    <div class="brand">
      <span class="brand-dot"></span>
      <span class="brand-name">Tornvale Communications</span>
    </div>
    <ul class="contact">
      <li><svg viewBox="0 0 10 10"><path d="M2 0.5l2 2-1 1.2c.6 1.3 1.5 2.2 2.8 2.8L7 5.5l2 2-1 1.8C4.5 9 1 5.5.7 1.5z"/></svg>1800 555 014</li>
      <li><svg viewBox="0 0 10 10"><path d="M0 2h10v6H0z M0 2l5 3.5L10 2" /></svg>info@tornvale-example.com.au</li>
      <li><svg viewBox="0 0 10 10"><circle cx="5" cy="5" r="4.5" fill="none" stroke="#e0693a" stroke-width="1"/><path d="M0.5 5h9M5 .5v9" stroke="#e0693a" stroke-width=".8"/></svg>tornvale-example.com.au</li>
    </ul>
  </header>

  <p class="date">Dated: February 15, 2023</p>

  <section class="body">
    <p class="salutation">Dear Sir,</p>
    <p>Lorem Ipsum is simply dummy text of the printing and typesetting industry. Lorem Ipsum has been the industry's standard dummy text ever since the 1500s, when an unknown printer took a galley of type and scrambled it to make a type specimen book. It has survived not only five centuries, but also the leap into electronic typesetting, remaining essentially unchanged. It was popularised in the 1960s with the release of Typeline sheets containing Lorem Ipsum passages, and more recently with desktop publishing software like Folio Layout including versions of Lorem Ipsum.</p>
    <p>It is a long established fact that a reader will be distracted by the readable content of a page when looking at its layout. The point of using Lorem Ipsum is that it has a more-or-less normal distribution of letters, as opposed to using 'Content here, content here', making it look like readable English. Many desktop publishing packages and web page editors now use Lorem Ipsum as their default model text, and a search for 'lorem ipsum' will uncover many web sites still in their infancy. Various versions have evolved over the years, sometimes by accident, sometimes on purpose (injected humour and the like).</p>
    <p class="last">The standard chunk of Lorem Ipsum used since the 1500s is reproduced below for those interested. Sections 1.10.32 and 1.10.33 from "de Finibus Bonorum et Malorum" by Marcus Tullen are also reproduced in their exact original form, accompanied by English versions from the 1914 translation by J. Ellory.</p>
  </section>

  <div class="signature" role="img" aria-label="Handwritten signature of the sender"></div>

  <footer>
    <p class="footer-address">PO Box 8164 Korrin Flats NSW 2419<span class="sep">|</span>ABN: 61 482 037 914</p>
    <div class="footer-bar">
      <span class="bar-orange"></span>
      <span class="bar-green"></span>
      <span class="bar-rust"></span>
    </div>
  </footer>
</main>
</body>
</html>
```